DeSIGN OF CARDS AND STATIONARY
MIRELLO VANTURA LAW
DeSIGN OF CARDS AND STATIONARY - Law
Creative Brief
Cutting-Edge
Rosalind Mirello Vantura
Criminal ATTORNEY
no address on the. card
rosalind@mirellovanturalaw.example
www.mirellovanturalaw.example
I. already. have. a logo I want to use
front of the. card will be the logo and name I send you. and in the back of the card will be. my info with logo. NEED TO ATTACH THE LOGO I JUST GOT.

```html
<!DOCTYPE html>
<html lang="en">
<head>
<meta charset="utf-8">
<title>Mirello Vantura Law — Cards and Stationery</title>
<link rel="stylesheet" href="https://fonts.googleapis.com/css2?family=Montserrat:wght@300;400;600&display=swap">
<style>
  :root{
    --bg:#ebebed;
    --paper:#ffffff;
    --navy:#1b1e4b;
    --navy-deep:#14163a;
    --accent:#5d73bb;
    --ink:#5c5f73;
    --ink-soft:#9a9cab;
    --rule:#b9b9c0;
  }
  *{box-sizing:border-box;margin:0;padding:0}
  html,body{width:1200px;height:528px;overflow:hidden;background:var(--bg);font-family:"Montserrat",sans-serif}
  .canvas{position:relative;width:1200px;height:528px}
  .piece{position:absolute;background:var(--paper);overflow:hidden;box-shadow:0 2px 6px rgba(0,0,0,.18)}
  .piece svg.shape{position:absolute;inset:0;width:100%;height:100%}
  .divider{position:absolute;left:396px;top:24px;width:1px;height:480px;background:var(--rule)}

  .wordmark{position:absolute;text-align:center;font-weight:400;letter-spacing:.22em;line-height:1.4;white-space:nowrap}
  .wordmark .dot{display:block;margin:0 auto 4px;border-radius:50%}

  /* business card front */
  .card-front{left:43px;top:91px;width:276px;height:156px}
  .card-front .wordmark{right:10px;top:26px;color:var(--paper);font-size:6.5px;width:100px}
  .card-front .wordmark .dot{width:14px;height:14px;border:1px solid var(--paper)}
  .card-front .holder{position:absolute;left:14px;top:64px;max-width:128px}
  .holder .name{font-size:6.5px;font-weight:600;color:var(--navy);letter-spacing:.03em;text-transform:uppercase;white-space:nowrap}
  .holder .role{font-size:5.5px;color:var(--ink-soft);margin-top:2px;letter-spacing:.05em}
  .holder ul{list-style:none;margin-top:10px}
  .holder li{display:flex;align-items:center;gap:5px;font-size:5px;color:var(--ink);margin-bottom:3px;white-space:nowrap}
  .icon{width:7px;height:7px;flex:none}

  /* business card back */
  .card-back{left:43px;top:271px;width:276px;height:156px;background:var(--navy)}
  .card-back .faint{position:absolute;left:40px;top:18px;width:120px;height:120px;border-radius:50%;background:rgba(255,255,255,.05)}
  .card-back .wordmark{left:0;right:0;top:62px;color:var(--paper);font-size:10px}
  .card-back .wordmark .dot{width:16px;height:16px;border:1px solid var(--accent)}

  /* letterhead */
  .letterhead{left:475px;top:65px;width:250px;height:427px}
  .letterhead .wordmark{left:0;right:0;top:22px;color:var(--navy);font-size:8px}
  .letterhead .wordmark .dot{width:16px;height:16px;border:1px solid var(--navy)}
  .contact-row{display:flex;justify-content:center;gap:10px;font-size:4.5px;color:var(--ink)}
  .contact-row span{display:flex;align-items:center;gap:3px;white-space:nowrap}
  .contact-row .icon{width:5px;height:5px}
  .letterhead .contact-row{position:absolute;left:0;right:0;top:72px}
  .letterhead .rule{position:absolute;left:20px;right:20px;top:84px;height:1px;background:var(--accent);opacity:.5}
  .letter{position:absolute;left:22px;right:22px;top:100px;font-size:5px;line-height:1.8;color:var(--ink)}
  .letter p{margin-bottom:7px}
  .letter .sign-off{margin-top:16px}
  .letter .signer{margin-top:22px;color:var(--navy);font-weight:600}

  /* compliment slip */
  .slip{left:821px;top:91px;width:333px;height:156px}
  .slip .wordmark{left:10px;top:28px;color:var(--paper);font-size:7px;width:110px}
  .slip .wordmark .dot{width:14px;height:14px;border:1px solid var(--paper)}
  .slip .contact-row{position:absolute;right:14px;top:92px;width:165px;flex-wrap:wrap;justify-content:flex-end;gap:4px 10px;font-size:4.5px}

  /* envelope */
  .envelope{left:821px;top:271px;width:333px;height:156px}
  .envelope .wordmark{left:0;right:0;top:16px;color:var(--paper);font-size:8px}
  .envelope .wordmark .dot{width:14px;height:14px;border:1px solid var(--paper)}
</style>
</head>
<body>
<main class="canvas">

  <section class="piece card-front">
    <svg class="shape" viewBox="0 0 276 156" preserveAspectRatio="none" aria-hidden="true">
      <path d="M182 0 C146 44 150 118 212 156 L276 156 L276 0 Z" fill="var(--accent)"/>
      <path d="M189 0 C154 44 158 116 220 156 L276 156 L276 0 Z" fill="var(--navy)"/>
    </svg>
    <div class="wordmark"><span class="dot"></span>MIRELLO VANTURA<br>LAW</div>
    <div class="holder">
      <p class="name">Rosalind Mirello Vantura</p>
      <p class="role">Criminal Attorney</p>
      <ul>
        <li><svg class="icon" viewBox="0 0 10 10"><path d="M2 1h2l1 2.5-1.3 1a5 5 0 0 0 2.8 2.8l1-1.3L10 7v2a1 1 0 0 1-1 1A8 8 0 0 1 0 2a1 1 0 0 1 1-1z" fill="var(--navy)"/></svg>(555) 014-2290</li>
        <li><svg class="icon" viewBox="0 0 10 10"><rect x="0.5" y="2" width="9" height="6" fill="none" stroke="var(--navy)"/><path d="M.5 2 5 5.5 9.5 2" fill="none" stroke="var(--navy)"/></svg>rosalind@mirellovanturalaw.example</li>
        <li><svg class="icon" viewBox="0 0 10 10"><circle cx="5" cy="5" r="4.3" fill="none" stroke="var(--navy)"/><path d="M.7 5h8.6M5 .7c-2.4 2.6-2.4 6 0 8.6M5 .7c2.4 2.6 2.4 6 0 8.6" fill="none" stroke="var(--navy)" stroke-width=".7"/></svg>www.mirellovanturalaw.example</li>
      </ul>
    </div>
  </section>

  <section class="piece card-back">
    <span class="faint"></span>
    <div class="wordmark"><span class="dot"></span>MIRELLO VANTURA<br>LAW</div>
  </section>

  <span class="divider"></span>

  <section class="piece letterhead">
    <div class="wordmark"><span class="dot"></span>MIRELLO VANTURA<br>LAW</div>
    <div class="contact-row">
      <span><svg class="icon" viewBox="0 0 10 10"><path d="M2 1h2l1 2.5-1.3 1a5 5 0 0 0 2.8 2.8l1-1.3L10 7v2a1 1 0 0 1-1 1A8 8 0 0 1 0 2a1 1 0 0 1 1-1z" fill="var(--navy)"/></svg>(555) 014-2290</span>
      <span><svg class="icon" viewBox="0 0 10 10"><rect x="0.5" y="2" width="9" height="6" fill="none" stroke="var(--navy)"/></svg>rosalind@mirellovanturalaw.example</span>
      <span><svg class="icon" viewBox="0 0 10 10"><circle cx="5" cy="5" r="4.3" fill="none" stroke="var(--navy)"/></svg>www.mirellovanturalaw.example</span>
    </div>
    <span class="rule"></span>
    <div class="letter">
      <p>Dear Mr. Doe,</p>
      <p>Thank you for meeting with our team this week. We have reviewed the documents you provided and prepared a summary of the next steps in your case. Please read it carefully and let us know of any questions.</p>
      <p>Our office will file the motion before the deadline and keep you informed at every stage. All conversations remain confidential.</p>
      <p>We look forward to working with you.</p>
      <p class="sign-off">Sincerely,</p>
      <p class="signer">Rosalind Mirello Vantura</p>
    </div>
  </section>

  <section class="piece slip">
    <svg class="shape" viewBox="0 0 333 156" preserveAspectRatio="none" aria-hidden="true">
      <path d="M130 0 C170 44 166 118 100 156 L0 156 L0 0 Z" fill="var(--accent)"/>
      <path d="M123 0 C162 44 158 116 93 156 L0 156 L0 0 Z" fill="var(--navy)"/>
    </svg>
    <div class="wordmark"><span class="dot"></span>MIRELLO VANTURA<br>LAW</div>
    <div class="contact-row">
      <span>(555) 014-2290</span>
      <span>rosalind@mirellovanturalaw.example</span>
      <span>www.mirellovanturalaw.example</span>
    </div>
  </section>

  <section class="piece envelope">
    <svg class="shape" viewBox="0 0 333 156" preserveAspectRatio="none" aria-hidden="true">
      <path d="M0 0 L333 0 L333 6 L178 84 Q166 90 154 84 L0 6 Z" fill="var(--accent)"/>
      <path d="M0 0 L333 0 L180 78 Q166 85 152 78 Z" fill="var(--navy)"/>
    </svg>
    <div class="wordmark"><span class="dot"></span>MIRELLO VANTURA<br>LAW</div>
  </section>

</main>
</body>
</html>
```